Small Business Broker Business Card Design

A business card design for a small business brokerage, which is a financial service, not unlike real estate brokerage, but for small businesses such as laundromats, pizza shops, restaurants, cleaners etc. The designs should all be simple, more conservative in nature, using the colors and font of the logo. Again, think real estate Brokerage as a business context
Contact Information for Business Card
Name: Dale R. Whitmore. Title: Small Business Advisor. Email: d.whitmore@lanternbridgeadvisory.com. Mobile: (917) 555-0148. Office: (718) 555-0193. www.lanternbridgeadvisory.com

```html
<!DOCTYPE html>
<html lang="en">
<head>
<meta charset="utf-8">
<title>Lanternbridge Advisory — Business Card</title>
<link rel="stylesheet" href="https://fonts.googleapis.com/css2?family=Montserrat:wght@500;600;700&display=swap">
<style>
  :root {
    --navy: #1d3a6b;
    --green: #8cc043;
    --paper: #ffffff;
    --backdrop: #e6e7ea;
    --font: "Montserrat", sans-serif;
  }
  * { box-sizing: border-box; margin: 0; padding: 0; }
  html, body { width: 1200px; height: 900px; overflow: hidden; }
  body {
    background: var(--backdrop);
    font-family: var(--font);
    display: flex;
    align-items: center;
    justify-content: center;
    gap: 40px;
  }
  .card {
    position: relative;
    width: 540px;
    height: 312px;
    background: var(--paper);
    box-shadow: 0 6px 18px rgba(0,0,0,0.18);
    overflow: hidden;
  }

  /* Front */
  .card--front {
    display: flex;
    flex-direction: column;
    align-items: center;
    justify-content: center;
    text-align: center;
  }
  .brand { display: flex; align-items: center; gap: 10px; }
  .brand__mark { width: 14px; height: 14px; background: var(--navy); }
  .brand__name {
    color: var(--navy);
    font-weight: 700;
    text-transform: uppercase;
    letter-spacing: 0.02em;
  }
  .brand__tagline {
    color: var(--green);
    font-weight: 600;
    text-transform: uppercase;
    letter-spacing: 0.1em;
  }
  .card--front .brand__name { font-size: 20px; }
  .card--front .brand__tagline { font-size: 10px; margin-top: 6px; }

  /* Back */
  .card--back .brand-block { position: absolute; left: 34px; top: 40px; }
  .card--back .brand__name { font-size: 19px; }
  .card--back .brand__tagline { font-size: 9.5px; margin-top: 3px; padding-left: 24px; }

  .person { position: absolute; left: 34px; top: 120px; }
  .person__name {
    color: var(--navy);
    font-size: 23px;
    font-weight: 700;
    text-transform: uppercase;
    letter-spacing: 0.02em;
  }
  .person__title {
    color: var(--green);
    font-size: 11.5px;
    font-weight: 600;
    text-transform: uppercase;
    letter-spacing: 0.04em;
    margin-top: 3px;
  }

  .contact {
    position: absolute;
    left: 34px;
    top: 186px;
    display: grid;
    grid-template-columns: 60px auto;
    row-gap: 3px;
    font-size: 13.5px;
    line-height: 16px;
    text-transform: uppercase;
  }
  .contact__label { color: var(--green); font-weight: 600; font-size: 11px; }
  .contact__value { color: var(--navy); font-weight: 600; }

  .footer-rule {
    position: absolute; left: 0; right: 0; top: 254px;
    height: 5px; background: var(--green);
  }
  .footer-band {
    position: absolute; left: 0; right: 0; top: 259px; bottom: 0;
    background: var(--navy);
    display: flex; align-items: center;
    padding-left: 34px;
  }
  .footer-band__url {
    color: var(--green);
    font-size: 13.5px;
    font-weight: 600;
    text-transform: uppercase;
    letter-spacing: 0.02em;
  }
</style>
</head>
<body>
  <section class="card card--front">
    <div class="brand">
      <span class="brand__mark"></span>
      <span class="brand__name">Lanternbridge Advisory, Inc</span>
    </div>
    <p class="brand__tagline">Confidently buy or sell a local business today</p>
  </section>

  <section class="card card--back">
    <div class="brand-block">
      <div class="brand">
        <span class="brand__mark"></span>
        <span class="brand__name">Lanternbridge Advisory, Inc</span>
      </div>
      <p class="brand__tagline">Confidently buy or sell a local business today</p>
    </div>

    <div class="person">
      <h1 class="person__name">Dale R. Whitmore</h1>
      <p class="person__title">Small Business Advisor</p>
    </div>

    <dl class="contact">
      <dt class="contact__label">Office:</dt><dd class="contact__value">(718) 555-0193</dd>
      <dt class="contact__label">Mobile:</dt><dd class="contact__value">(917) 555-0148</dd>
      <dt class="contact__label">Email:</dt><dd class="contact__value">d.whitmore@lanternbridgeadvisory.com</dd>
    </dl>

    <div class="footer-rule"></div>
    <div class="footer-band">
      <span class="footer-band__url">www.lanternbridgeadvisory.com</span>
    </div>
  </section>
</body>
</html>
```